Harbor Tandem Web Design Project

We need a website design for a start up company called "Harbor Tandem". We provide business consultancy services as well as technology-related services (IT). The design should communicate simplicity and elegance. The domain name of the site will be harbortandem.com. The logo of the company is https://files.pinvault.net/u/8147206/7730_2049185_31947_image.jpg
Updates

Target Market(s)

SMB, Corporates, Semi-governments, Governments.

Industry/Entity Type

Business

Requirements
Must have
• - The background of the pages should be white or soft grey, but we are open for suggestions.
- The pages should have nice menu animations.
- The pages should be "portal-style", with multiple placeholders for different sections and multiple tabs.
Nice to have
• The page should auto-fit the screen and scroll vertically as much as needed.
Should not have
• - Flash Animations.
- Generic Photos.

```html
<!DOCTYPE html>
<html lang="en">
<head>
<meta charset="utf-8">
<title>Harbor Tandem</title>
<link rel="stylesheet" href="https://fonts.googleapis.com/css2?family=Questrial&family=Arimo:wght@400;700&family=Open+Sans:wght@600;700&display=swap">
<style>
:root{
  --red:#d81e24;
  --red-dark:#b5161b;
  --blue:#1d5ca8;
  --blue-bright:#0a7fd0;
  --grey-text:#555;
  --grey-head:#6b6b6b;
  --bg:#ebebeb;
  --light:#f6f6f6;
  --line:#d2d2d2;
  --white:#fff;
}
*{margin:0;padding:0;box-sizing:border-box}
html,body{width:974px;height:1200px;overflow:hidden}
body{background:var(--bg);font-family:"Arimo",Arial,sans-serif;color:var(--grey-text);position:relative}
.page{position:absolute;inset:0;background:linear-gradient(#f7f7f7,#ececec 60%,#e8e8e8)}
.abs{position:absolute}

/* top bar */
.topbar{left:133px;top:0;width:710px;height:38px;border-bottom:1px solid var(--line)}
.topbar .welcome{position:absolute;left:1px;top:14px;font-size:9px;color:#9a9a9a;text-transform:uppercase}
.topbar .links{position:absolute;right:222px;top:14px;font-size:10px;color:#8a8a8a;letter-spacing:.3px}
.topbar .links span{margin:0 6px;color:#ccc}
.search{position:absolute;right:0;top:9px;width:158px;height:21px;border-radius:11px;background:var(--white);border:1px solid #ddd;box-shadow:inset 0 1px 2px rgba(0,0,0,.08)}
.search svg{position:absolute;right:7px;top:5px}

/* header */
.brand{left:138px;top:78px;display:flex;align-items:center;gap:9px}
.brand-mark{width:22px;height:22px;border-radius:50%;background:var(--blue)}
.brand-name{font-family:"Questrial",sans-serif;font-size:24px;color:var(--red)}
.nav{left:506px;top:92px;font-family:"Questrial",sans-serif;font-size:11px;color:var(--red);text-transform:uppercase;display:flex;gap:0}
.nav a{color:inherit;text-decoration:none;padding:0 10px;border-left:1px solid #e4b7b8;line-height:12px}
.nav a:first-child{border-left:none;padding-left:0}

/* hero */
.hero{left:0;top:158px;width:974px;height:237px;background:linear-gradient(var(--red),var(--red-dark))}
.hero-rule{left:0;top:393px;width:974px;height:4px;background:var(--blue)}
.hero-title{left:0;top:196px;width:974px;text-align:center;font-family:"Questrial",sans-serif;font-size:104px;line-height:1;color:var(--white);letter-spacing:-2px;text-shadow:0 2px 4px rgba(0,0,0,.18)}
.hero-sub{left:0;top:295px;width:974px;text-align:center;font-family:"Open Sans",sans-serif;font-weight:600;font-size:8px;color:var(--white)}

/* portal cards */
.card{top:345px;width:233px;height:156px;background:linear-gradient(#fdfdfd,#ececec);border-bottom:6px solid #a9a9a9;box-shadow:0 10px 12px -8px rgba(0,0,0,.25)}
.card .art{position:absolute;left:56px;top:-21px;width:120px;height:110px;border-radius:6px}
.card .label{position:absolute;left:0;bottom:14px;width:100%;text-align:center;font-family:"Questrial",sans-serif;font-size:17px;color:#777;letter-spacing:-.5px;text-transform:uppercase}

/* welcome */
.welcome-head{left:133px;top:546px;font-family:"Questrial",sans-serif;font-size:32px;line-height:1;color:var(--blue);letter-spacing:-1px}
.welcome-sub{left:133px;top:582px;width:194px;text-align:right;font-family:"Questrial",sans-serif;font-size:18px;color:var(--red)}
.welcome-div{left:353px;top:551px;width:1px;height:84px;background:var(--line)}
.welcome-lead{left:371px;top:550px;width:460px;font-family:"Questrial",sans-serif;font-size:18px;line-height:21px;color:var(--blue-bright);letter-spacing:-.4px}
.welcome-body{left:371px;top:605px;width:470px;font-size:8.6px;line-height:11.5px;color:#555}

/* call to action */
.cta{left:0;top:660px;width:974px;height:70px;background:var(--light);border-top:1px solid var(--line);border-bottom:1px solid var(--line)}
.cta-text{left:133px;top:683px;font-family:"Questrial",sans-serif;font-size:18px;color:var(--red);letter-spacing:-.5px}
.cta-btn{left:637px;top:676px;width:200px;height:39px;background:var(--blue);color:var(--white);font-family:"Questrial",sans-serif;font-size:14.5px;display:flex;align-items:center;justify-content:center;gap:9px;text-transform:uppercase;letter-spacing:-.3px}

/* info columns */
.col-head{top:770px;font-family:"Questrial",sans-serif;font-size:21px;color:var(--grey-head);letter-spacing:-1px;text-transform:uppercase}
.col-head.blue{color:var(--blue)}
.col-div{top:770px;width:1px;height:152px;background:var(--line)}
.services{left:135px;top:807px;list-style:none;font-size:8.3px;color:#444}
.services li{height:20.5px;padding-left:11px;position:relative}
.services li::before{content:"";position:absolute;left:0;top:2px;width:5px;height:5px;background:linear-gradient(135deg,var(--blue) 50%,var(--red) 50%)}
.stories{left:371px;top:807px;width:218px;font-size:8.3px;line-height:11.2px;color:#555}
.stories p+p{margin-top:14px}
.stories a{color:#222;font-weight:700;text-decoration:underline}
.grow{left:629px;top:810px;width:167px;list-style:none;font-size:8.3px;color:var(--red)}
.grow li{display:flex;align-items:center;gap:9px;height:23.5px;border-bottom:1px dotted #ccc}
.grow li:last-child{border-bottom:none}
.grow svg{flex:none}
.readmore{top:937px;font-family:"Questrial",sans-serif;font-size:12px;color:#999;text-decoration:underline}

/* footer */
.foot-rule{left:0;top:977px;width:974px;height:3px;background:var(--red)}
.footer{left:0;top:982px;width:974px;height:180px;background:radial-gradient(ellipse at 45% 10%,#1b8fd8,var(--blue) 75%)}
.foot-head{top:1001px;font-family:"Questrial",sans-serif;font-size:18px;color:var(--white);letter-spacing:-.6px}
.foot-div{top:1004px;width:1px;height:134px;background:rgba(255,255,255,.18)}
.quick{left:136px;top:1036px;list-style:none;font-size:8.3px;line-height:12.9px;color:var(--white)}
.contact{left:281px;top:1035px;font-size:8.3px;line-height:15px;color:var(--white)}
.phone{left:278px;top:1075px;display:flex;align-items:center;gap:6px;font-family:"Questrial",sans-serif;font-size:19px;color:var(--white);letter-spacing:-.7px}
.phone .disc{width:26px;height:26px;border-radius:50%;background:#e9e9e9;display:flex;align-items:center;justify-content:center}
.news{left:484px;top:1035px;width:210px;font-size:8.3px;line-height:15px;color:var(--white)}
.news-form{left:484px;top:1075px;width:205px;height:20px;display:flex;border-radius:10px;overflow:hidden}
.news-form .field{flex:1;background:var(--white)}
.news-form .btn{width:50px;background:var(--red);color:var(--white);font-size:7px;display:flex;align-items:center;justify-content:center;border-radius:10px 0 0 10px;margin-left:-8px}
.social{left:723px;top:1037px;display:flex;gap:7px}
.social i{display:block;width:12px;height:12px;border-radius:50%;background:var(--white)}
.copy{left:137px;top:1173px;font-size:8.3px;color:#888}
</style>
</head>
<body>
<div class="page">

  <div class="abs topbar">
    <div class="welcome">Welcome to Harbor Tandem</div>
    <div class="links">LOGIN<span>|</span>HELP</div>
    <div class="search"><svg width="7" height="7" viewBox="0 0 10 10"><circle cx="4" cy="4" r="3" fill="none" stroke="#666" stroke-width="1.6"/><path d="M6 6l3 3" stroke="#666" stroke-width="1.6"/></svg></div>
  </div>

  <div class="abs brand"><span class="brand-mark"></span><span class="brand-name">Harbor Tandem</span></div>

  <nav class="abs nav">
    <a href="#">Home</a><a href="#">About us</a><a href="#">Services</a><a href="#">Solutions</a><a href="#">Contacts</a>
  </nav>

  <div class="abs hero"></div>
  <div class="abs hero-rule"></div>
  <h1 class="abs hero-title">DEVELOP</h1>
  <p class="abs hero-sub">B2B and B2C SAAS based solutions and e-commerce portals for companies</p>

  <div class="abs card" style="left:131px">
    <div class="art" role="img" aria-label="Illustration of a globe beside a travel bag" style="background:radial-gradient(circle at 40% 55%,#4a9ad0,#6f7a5e 55%,transparent 72%)"></div>
    <div class="label">B2B Portals</div>
  </div>
  <div class="abs card" style="left:371px">
    <div class="art" role="img" aria-label="Illustration of two business people" style="background:radial-gradient(circle at 50% 55%,#3c4f8a,#444 50%,transparent 72%)"></div>
    <div class="label">B2C Portals</div>
  </div>
  <div class="abs card" style="left:610px">
    <div class="art" role="img" aria-label="Illustration of a paper shopping bag" style="background:radial-gradient(circle at 50% 55%,#cfc8b0,#b9b29a 50%,transparent 72%)"></div>
    <div class="label">E-Commerce Portals</div>
  </div>

  <h2 class="abs welcome-head">WELCOME TO</h2>
  <div class="abs welcome-sub">Harbor Tandem</div>
  <div class="abs welcome-div"></div>
  <p class="abs welcome-lead">We are proud to deliver immediate results through active skills, and real-world tasks ...</p>
  <p class="abs welcome-body">Lorem ipsum dolor sit amet, consectetuer adipiscing elit, sed diam nonummy nibh euismod tincidunt ut laoreet dolore magna aliquam erat volutpat. Ut wisi enim ad minim veniam, quis nostrud exerci tation ullamcorper suscipit lobortis nisl ut aliquip ex ea commodo consequat.</p>

  <div class="abs cta"></div>
  <div class="abs cta-text">Are you interested in our offer? Do you have any questions?</div>
  <a class="abs cta-btn">Get in touch with us
    <svg width="18" height="13" viewBox="0 0 18 13"><rect x="1" y="1" width="16" height="11" fill="none" stroke="#fff" stroke-width="1.4"/><path d="M1 1l8 6 8-6" fill="none" stroke="#fff" stroke-width="1.4"/></svg>
  </a>

  <h3 class="abs col-head" style="left:132px">Our Services</h3>
  <div class="abs col-div" style="left:353px"></div>
  <h3 class="abs col-head" style="left:371px">Success Stories</h3>
  <div class="abs col-div" style="left:607px"></div>
  <h3 class="abs col-head blue" style="left:628px">Grow Your Business</h3>

  <ul class="abs services">
    <li>Lorem ipsum dolor sit amet, consectetuer....</li>
    <li>Adipiscing elit, sed diam nonummy</li>
    <li>Nibh euismod tincidunt ut laoreet dolore</li>
    <li>Ut wisi enim ad minim veniam, quis nostrud</li>
    <li>Exerci tation ullamcorper suscipit lobortis nisl</li>
    <li>Ut aliquip ex ea commodo consequat.</li>
  </ul>

  <div class="abs stories">
    <p>Lorem ipsum dolor sit amet, consectetuer adipiscing elit, sed diam nonummy nibh euismod tincidunt ut laoreet dolore magna aliquam erat volutpat. Ut wisi enim ad minim veniam, quis nostrud exerci tation ullamcorper suscipit lobortis nisl ut aliquip ex ea commodo consequat.</p>
    <p>We have completed some really interesting projects recently. You can take a look at a selection of our projects in our <a href="#">portfolio</a> section.</p>
  </div>

  <ul class="abs grow">
    <li><svg width="16" height="16" viewBox="0 0 16 16"><rect x="1" y="1" width="14" height="14" fill="none" stroke="#d81e24" stroke-width="2"/><path d="M1 6h14M1 10.5h14M6 1v14M10.5 1v14" stroke="#d81e24" stroke-width="1.6"/></svg>Customised selling platform</li>
    <li><svg width="16" height="16" viewBox="0 0 16 16"><rect x="1" y="1" width="14" height="14" fill="none" stroke="#d81e24" stroke-width="1.5"/><path d="M4 13l4-10 4 10M5.5 9h5" fill="none" stroke="#d81e24" stroke-width="1.5"/></svg>Unique designs, every time</li>
    <li><svg width="16" height="16" viewBox="0 0 16 16"><circle cx="5" cy="5" r="2.5" fill="#d81e24"/><circle cx="11" cy="5" r="2.5" fill="#d81e24"/><path d="M1 15c0-4 2-6 4-6s4 2 4 6zM7 15c0-4 2-6 4-6s4 2 4 6z" fill="#d81e24"/></svg>We focus on your customers</li>
    <li><svg width="16" height="16" viewBox="0 0 16 16"><path d="M1 2h3l2 8h8l1-6H5" fill="none" stroke="#d81e24" stroke-width="1.5"/><circle cx="7" cy="13.5" r="1.4" fill="#d81e24"/><circle cx="13" cy="13.5" r="1.4" fill="#d81e24"/></svg>Easy to use order process</li>
    <li><svg width="18" height="16" viewBox="0 0 18 16"><rect x="1" y="2" width="12" height="9" fill="none" stroke="#d81e24" stroke-width="2"/><path d="M5 14h4" stroke="#d81e24" stroke-width="2"/><rect x="14" y="4" width="3" height="10" fill="#d81e24"/></svg>Reliable</li>
  </ul>

  <a class="abs readmore" style="left:147px">readmore..</a>
  <a class="abs readmore" style="left:371px">readmore..</a>
  <a class="abs readmore" style="left:631px">readmore..</a>

  <div class="abs foot-rule"></div>
  <footer class="abs footer"></footer>

  <h4 class="abs foot-head" style="left:132px">Quick Links</h4>
  <div class="abs foot-div" style="left:265px"></div>
  <h4 class="abs foot-head" style="left:281px">Harbor Tandem</h4>
  <div class="abs foot-div" style="left:466px"></div>
  <h4 class="abs foot-head" style="left:484px">Join Our Newsletter</h4>
  <div class="abs foot-div" style="left:705px"></div>
  <h4 class="abs foot-head" style="left:723px">Follow Us</h4>

  <ul class="abs quick">
    <li>Blog</li><li>Website design</li><li>Website package</li><li>Website hosting</li>
    <li>Content management system</li><li>Search Engine Optimisation</li><li>Ecommerce &amp; online stores</li><li>Social Media Marketing</li>
  </ul>

  <div class="abs contact">42 Linden Row, Elm Hollow, Westfield, WF3 7QD<br>info@harbortandem.com</div>
  <div class="abs phone">
    <span class="disc"><svg width="12" height="14" viewBox="0 0 12 14"><path d="M3 1l2 3-1.5 1.5c.6 2 1.8 3.4 3.5 4.4L8.5 8.5l3 2-1.5 2.5C5.5 12.5 1.5 7.5 1 2.5z" fill="#666"/></svg></span>
    0800-2040-300
  </div>

  <p class="abs news">Stay up to date with all our latest tips to improve your websites performance with our newsletter.</p>
  <div class="abs news-form"><span class="field"></span><span class="btn">Subscribe</span></div>

  <div class="abs social"><i></i><i></i><i></i><i></i><i></i></div>

  <p class="abs copy">Copyright © 2012 HarborTandem.  All rights reserved.</p>
</div>
</body>
</html>
```